Coral Tide Foundation and Brenmor Foundation are holding the first 'Brushes for Tomorrow' contest.

I need a flyer/poster created about the art contest to post in schools across the state of Hawaii for grades K-12. We are trying to engage and inspire youth to learn more about this critically endangered species and it's important role to Hawaii's ecosystem. The art contest will be from March 27 - April 11, 2014. One winner from each grade will be selected and announced by late May. Students will create ‘The Hawaiian Monk Seal, a living treasure’ through paint, drawing, collage or sculpture. Art medium can include: chalk, charcoal, clay, crayon, marker, paint, pen, pencil or watercolor. Students can register and submit original artwork at to www.coraltidefoundation.org/artcontest.
I need to have this flyer in a photoshop file with layers in tact so I can edit it for future years. It is imperative to incorporate each logo into the design (please let me know if you require different format? png vs. jpeg)

• Both logos for foundations, convey that this is an art contest, dates of contest and how to submit artwork.

```html
<!DOCTYPE html>
<html lang="en">
<head>
<meta charset="utf-8">
<title>Brushes for Tomorrow – Art Contest Poster</title>
<link rel="stylesheet" href="https://fonts.googleapis.com/css2?family=Arimo:wght@400;700&family=Fredoka:wght@500;600&family=Righteous&display=swap">
<style>
  :root {
    --page: #ffffff;
    --navy: #0b2a6e;
    --navy-deep: #0a2466;
    --ocean-light: #3fb4ee;
    --ocean-mid: #1a6fd0;
    --ocean-deep: #0b3a9a;
    --art-white: #f4f8ff;
    --art-lilac: #c98ee6;
    --art-teal: #5fd6d0;
    --yellow: #f5ec1a;
    --white: #ffffff;
    --link: #36b6f0;
    --footer-ink: #1b2f73;
  }
  * { margin: 0; padding: 0; box-sizing: border-box; }
  html, body { width: 1200px; height: 1000px; overflow: hidden; background: var(--page); }
  .canvas { position: relative; width: 1200px; height: 1000px; }

  .poster {
    position: absolute; left: 293px; top: 40px; width: 613px; height: 918px;
    background: var(--page); overflow: hidden;
  }
  .ocean {
    position: absolute; left: 0; top: 0; width: 613px; height: 768px;
    background:
      radial-gradient(ellipse 55% 40% at 35% 55%, rgba(120,220,255,.7), rgba(120,220,255,0) 70%),
      linear-gradient(180deg, var(--ocean-light) 0%, var(--ocean-mid) 55%, var(--ocean-deep) 100%);
  }
  .seal-artwork {
    position: absolute; left: 30px; top: 262px; width: 480px; height: 410px;
    border-radius: 50%;
    border: 3px solid rgba(201,142,230,.75);
    box-shadow: 0 0 0 10px rgba(95,214,208,.25), 0 0 0 22px rgba(201,142,230,.18);
    background:
      radial-gradient(circle at 50% 50%, var(--art-white) 0%, var(--art-white) 22%, rgba(244,248,255,.7) 34%, rgba(95,214,208,.55) 55%, rgba(201,142,230,.6) 78%, rgba(201,142,230,.35) 100%);
  }

  .band { position: absolute; background: var(--navy); }
  .band--title { left: 0; top: 5px; width: 452px; height: 215px; }
  .band--contest { left: 282px; top: 135px; width: 300px; height: 85px; }
  .band--date { left: 192px; top: 218px; width: 390px; height: 46px; }
  .band--caption { left: 95px; top: 662px; width: 420px; height: 94px; opacity: .9; }

  .title {
    position: absolute; left: 12px; top: 38px; width: 440px;
    font-family: "Righteous", sans-serif; font-size: 60px; line-height: 54px;
    color: var(--white); letter-spacing: -1px;
  }
  .contest-label {
    position: absolute; left: 290px; top: 135px;
    font-family: "Fredoka", sans-serif; font-weight: 600; color: var(--yellow);
    transform: rotate(-4deg); transform-origin: left top;
  }
  .contest-label__name { display: block; font-size: 37px; line-height: 40px; }
  .contest-label__grades { display: block; font-size: 21px; line-height: 24px; margin-left: 20px; }

  .dates {
    position: absolute; left: 204px; top: 220px;
    font-family: "Fredoka", sans-serif; font-weight: 600; font-size: 34px; line-height: 42px;
    color: var(--white);
  }
  .caption {
    position: absolute; left: 95px; top: 666px; width: 420px; text-align: center;
    font-family: "Arimo", sans-serif; font-size: 22px; line-height: 28px; color: var(--yellow);
  }
  .caption strong { font-weight: 700; }

  .info {
    position: absolute; left: 0; top: 768px; width: 613px; height: 64px;
    background: var(--navy-deep); color: var(--white); text-align: center;
    font-family: "Arimo", sans-serif; font-size: 12.5px; line-height: 21px; padding-top: 11px;
  }
  .info strong { font-weight: 700; }
  .info__link { color: var(--link); font-weight: 700; }

  .partners {
    position: absolute; left: 0; top: 832px; width: 613px; height: 86px; background: var(--page);
  }
  .partner-name {
    position: absolute; font-family: "Arimo", sans-serif; font-weight: 400; color: var(--footer-ink);
  }
  .partner-name--brenmor { left: 37px; top: 27px; font-size: 30px; letter-spacing: 1px; }
  .partner-name--coral { left: 450px; top: 28px; font-size: 14px; line-height: 16px; text-align: center; width: 125px; }
</style>
</head>
<body>
<div class="canvas">
  <section class="poster">
    <div class="ocean" role="img" aria-label="Underwater ocean photograph in bright blues with light from the surface"></div>
    <div class="seal-artwork" role="img" aria-label="Illustration of four white monk seal silhouettes swimming in a circle over lilac, teal and red ripple rings"></div>

    <div class="band band--title"></div>
    <div class="band band--contest"></div>
    <div class="band band--date"></div>
    <div class="band band--caption"></div>

    <h1 class="title">Brushes<br>for<br>Tomorrow</h1>
    <p class="contest-label">
      <span class="contest-label__name">ART CONTEST</span>
      <span class="contest-label__grades">OPEN TO GRADES K-12</span>
    </p>
    <p class="dates">March 27 · April 11, 2014</p>

    <p class="caption">Create ‘<strong>The Hawaiian Monk Seal, a<br>living treasure</strong>’ through paint, drawing,<br>collage or sculpture.</p>

    <div class="info">
      <p>Art medium can include: <strong>chalk, charcoal, clay, crayon, marker, paint, pen, pencil or watercolor</strong>.</p>
      <p>Register and submit original artwork at to <span class="info__link">www.coraltidefoundation.org/artcontest</span></p>
    </div>

    <footer class="partners">
      <span class="partner-name partner-name--brenmor">BRENMOR FOUNDATION</span>
      <span class="partner-name partner-name--coral">CORAL TIDE FOUNDATION</span>
    </footer>
  </section>
</div>
</body>
</html>
```